Print & digital package needed for technology firm

We need a package of coordinating marketing materials for our technology business. We offer technology solutions to midsized organizations, including data center, outsourced IT, and technology consulting. Find more information on our website, www.pexlora.com. Design is the main concern, we can modify the text ongoing to best reflect our company’s offerings. The design should communicate technology expertise and strategic thinking. Our website is currently being updated with a “flat design” theme and we’d like design of these items to be flat, fresh, modern, and professional, without being boring.
Please use attached logo - can send in .ai/.eps/.psd/etc. Fonts in logo are Futura, Futura Book, and Lato. Please use pexLORA blue, #0372bb.
Please find attached one of our product flyers for one of the computers we lease. Fonts used are Roboto Slab (partial to this font) & Lato. Also attached copy of our business card design.
Taglines we have used include “Does IT hear what troubles you?” and “IT made simple” although we are open to new ideas.
Would like final products to be available in editable files - .psd/.tif/.ai/etc.

- 1 PowerPoint template
- 1 leaderboard ad (digital, 72dpi)
- 1 medium rectangle ad 300x250 (digital, 72dpi)
- 1 full page ad 8x11 (print, 300dpi)
- 1 half-page ad horizontal (print, 300dpi)
- 1 letterhead template
- 1 proposal front-page

There is potential for further graphic/print design opportunities for our business as well.

All, thank you for your assistance in understanding the budget process with this type of design contest - we have updated the project's budget to reflect the items we are requesting.

Please email mvarga at pexlora.com with inquiries or comments. Thank you.

Designers,

Due to an oversight, our project was listed as "refundable" - this has been corrected and changed to committed payment.
To enter into this contest, please pick 2-3 items from the list of desired materials (ads, powerpoint, letterhead, etc.) It is not necessary to submit all items which will be part of the final package to be considered for the contest.

Thank you. Please contact mvarga@pexlora.com for questions.
Best,
Mimi

CEOs, CFOs, CIOs, COOs - college+ educated, 30-60, professional.

```html
<!DOCTYPE html>
<html lang="en">
<head>
<meta charset="utf-8">
<title>Pexlora – Proposal Front Page</title>
<link rel="stylesheet" href="https://fonts.googleapis.com/css2?family=Lato:ital,wght@0,300;0,400;0,700;1,300;1,400&display=swap">
<style>
  :root {
    --brand-blue: #0372bb;
    --band-blue: #1470bd;
    --white: #ffffff;
    --ink: #1d1d1f;
    --muted: #555a60;
    --ember-dark: #9e3412;
    --ember: #c4511c;
    --flame: #f08a22;
  }
  * { box-sizing: border-box; margin: 0; padding: 0; }
  html, body { width: 873px; height: 1200px; overflow: hidden; background: var(--white); }
  .cover {
    position: relative;
    width: 873px;
    height: 1200px;
    overflow: hidden;
    font-family: 'Lato', sans-serif;
    color: var(--white);
  }
  .cover__backdrop {
    position: absolute;
    inset: 0;
    background:
      radial-gradient(ellipse 420px 380px at 800px 760px, rgba(255,244,210,0.95) 0%, rgba(255,190,90,0.75) 35%, rgba(240,138,34,0) 75%),
      radial-gradient(ellipse 500px 420px at 760px 1050px, rgba(255,236,200,0.9) 0%, rgba(248,170,70,0.6) 45%, rgba(240,138,34,0) 80%),
      radial-gradient(ellipse 520px 420px at 150px 120px, rgba(232,110,40,0.7) 0%, rgba(196,81,28,0) 80%),
      linear-gradient(160deg, var(--ember) 0%, #b4441a 35%, var(--ember-dark) 55%, var(--flame) 85%, #f4a445 100%);
  }
  .marker {
    position: absolute;
    left: 617px;
    top: 0;
    width: 137px;
    height: 198px;
    background: var(--band-blue);
  }
  .marker__ring {
    position: absolute;
    left: 17px;
    top: 64px;
    width: 104px;
    height: 104px;
    border: 2px solid var(--white);
    border-radius: 50%;
  }
  .cover__title {
    position: absolute;
    left: 76px;
    top: 398px;
    font-weight: 400;
    font-size: 104px;
    line-height: 100px;
    letter-spacing: 0;
  }
  .brand-card {
    position: absolute;
    left: 625px;
    top: 803px;
    width: 260px;
    height: 155px;
    background: var(--white);
    border: 2px solid var(--brand-blue);
    border-radius: 30px 0 0 30px;
    padding: 54px 12px 0 12px;
    text-align: center;
  }
  .brand-card__name {
    font-size: 34px;
    font-weight: 400;
    color: var(--ink);
    line-height: 1;
    padding-right: 12px;
  }
  .brand-card__services {
    margin-top: 10px;
    font-size: 11px;
    color: var(--muted);
    white-space: nowrap;
    padding-right: 12px;
  }
  .band__tab {
    position: absolute;
    left: 0;
    top: 871px;
    width: 57px;
    height: 91px;
    background: var(--band-blue);
    border-top-right-radius: 24px;
  }
  .band {
    position: absolute;
    left: 57px;
    top: 961px;
    width: 570px;
    height: 127px;
    background: var(--band-blue);
    border-radius: 0 0 24px 24px;
    padding: 18px 20px 0 46px;
  }
  .band__tagline {
    font-size: 31px;
    font-style: italic;
    font-weight: 300;
    line-height: 1.1;
  }
  .band__copy {
    margin-top: 12px;
    font-size: 8.4px;
    line-height: 1.45;
    width: 502px;
  }
</style>
</head>
<body>
  <main class="cover">
    <div class="cover__backdrop" role="img" aria-label="Abstract orange and amber technology artwork with glowing light streaks and grid lines"></div>

    <div class="marker" aria-hidden="true">
      <div class="marker__ring"></div>
    </div>

    <h1 class="cover__title">PROPOSAL<br>TITLE</h1>

    <div class="brand-card">
      <div class="brand-card__name">Pexlora</div>
      <div class="brand-card__services">Consulting &nbsp;·&nbsp; Support &nbsp;·&nbsp; Hosting</div>
    </div>

    <div class="band__tab"></div>
    <section class="band">
      <p class="band__tagline">IT made simple!</p>
      <p class="band__copy">Quisque interdum nunc non velit euismod sit amet dictum diam lacinia. Vestibulum est lacus, ultricies a scelerisque et, accumsan ut quam. Aliquam id sapien sed urna tempus hendrerit. Curabitur lobortis justo sed risus consectetur dapibus. Mauris molestie velit ut turpis sodales viverra. Nam eu libero diam, a rutrum dolor. Cras eu nibh arcu. Morbi ac felis justo, eu vehicula justo.</p>
    </section>
  </main>
</body>
</html>
```